Book Cover Contest: "Rivers Toward a Calm Dawn"

The KT Verlag Islamic Library invites designers and artists to design a cover for the upcoming book “Rivers Toward a Calm Dawn”.

This inspiring work is by Shaikh Umar al-Fadil ibn Yusuf ibn Hamzah al-Qurtubi (d. 1376 AH/1957 CE), a renowned Islamic scholar. In his writing, he imparts timeless principles for inner peace and true happiness based on Islamic faith and spiritual knowledge.

Important details for the cover design:
The cover should reflect the theme of the book: paths to happiness, spiritual satisfaction, a fulfilled life.
It may contain both modern and traditional elements, but should be clear, appealing and reader-friendly.
The title “Rivers toward a calm dawn” should be clearly visible.
Author: Šaiḫ ʿUmar al-Fāḍil ibn Yūsuf ibn Ḥamzah al-Qurṭubī
Translation: Marita Lohse

KT Verlag Islamic Library

Do you have a creative idea for the cover? Then join in and design the face of this inspiring work!

Target Market(s)

Islamic

Font styles to use
Decorative
Script

Requirements
Should not have
• No mosque silhouette, no hanging lamp,

```html
<!DOCTYPE html>
<html lang="de">
<head>
<meta charset="utf-8">
<title>Flüsse zu einem stillen Morgen – Buchcover</title>
<link rel="stylesheet" href="https://fonts.googleapis.com/css2?family=Cinzel:wght@500;600;700&display=swap">
<style>
  :root {
    --backdrop: #b1b1b1;
    --title-blue: #283a8a;
    --title-black: #111111;
    --author-white: #ffffff;
    --sky-pink: #e8b2b6;
    --sky-peach: #f6d7a6;
    --sky-pale: #f9efb2;
    --sky-gold: #f6dc8c;
    --sun-orange: #f2993f;
    --hill-violet: #7d82b4;
    --hill-blue: #4a5a9c;
    --hill-navy: #1d285e;
  }
  html, body {
    margin: 0;
    width: 1200px;
    height: 1200px;
    overflow: hidden;
    background: var(--backdrop);
  }
  .book-cover {
    position: absolute;
    left: 240px;
    top: 60px;
    width: 720px;
    height: 1081px;
    overflow: hidden;
    box-shadow: 3px 3px 4px rgba(0, 0, 0, 0.25);
  }
  .cover-artwork {
    position: absolute;
    inset: 0;
    background: linear-gradient(
      to bottom,
      var(--sky-pink) 0%,
      var(--sky-peach) 14%,
      var(--sky-pale) 38%,
      var(--sky-gold) 55%,
      var(--sky-pale) 64%,
      var(--sun-orange) 74%,
      var(--hill-violet) 80%,
      var(--hill-blue) 87%,
      var(--hill-navy) 100%
    );
  }
  .cover-type {
    position: absolute;
    inset: 0;
    width: 720px;
    height: 1081px;
    font-family: "Cinzel", "Times New Roman", serif;
  }
  .title-main { fill: var(--title-blue); font-weight: 700; }
  .title-sub { fill: var(--title-black); font-weight: 600; }
  .author-name { fill: var(--author-white); font-weight: 500; }
</style>
</head>
<body>
  <main class="book-cover">
    <div class="cover-artwork" role="img" aria-label="Watercolour sunset over layered blue hills, with dark plant silhouettes in the foreground"></div>
    <svg class="cover-type" viewBox="0 0 720 1081" aria-label="Flüsse zu einem stillen Morgen">
      <text class="title-main" x="131" y="168" font-size="157" textLength="458" lengthAdjust="spacingAndGlyphs">FLÜSSE</text>
      <text class="title-sub" x="139" y="247" font-size="84" textLength="449" lengthAdjust="spacingAndGlyphs">ZU EINEM</text>
      <text class="title-sub" x="136" y="317" font-size="53" textLength="447" lengthAdjust="spacing">STILLEN</text>
      <text class="title-main" x="58" y="486" font-size="205" textLength="604" lengthAdjust="spacingAndGlyphs">MORGEN</text>
      <text class="author-name" x="139" y="1020" font-size="45" textLength="444" lengthAdjust="spacing">AUTHOR NAME</text>
    </svg>
  </main>
</body>
</html>
```